Door Hanger General Contractor

design high quality marketing piece to promote our general contractor business.
Use all content create badges, banners, bubbles, boxes ect to highlight text.
Template format is uploaded in images
Make font as large as possible, minimize negative space, fill areas
FRONT SIDE
Your Neighbor Just Remodeled
Come See Our Work at:
(under this create blank white box placeholder for address)
LOVE YOUR HOME AGAIN!
WE MAKE REMODELING EASY
FREE 3D DESIGN SERVICES
FREE ESTIMATES
LICENSED GENERAL CONTRACTORS
We Specialize in:
Kitchen Remodel
Bathroom Remodel
Interior/Exterior Painting
Flooring: Carpet, Vinyl, Wood & Tile
Energy Efficient Upgrades
Window/Door Replacement
WATER & MOLD DAMAGE
BACK SIDE
GET STARTED IN 3 SIMPLE STEPS:
1 ORDER FREE ESTIMATE & DESIGN
2 APPROVE ESTIMATE & DESIGN
3 HEARTHWAY RENOVATORS BUILDS YOUR DREAM
Thinking About Selling?
We Buy Homes
GET CASH OFFER
SELLING MADE EASY
CALL NOW!!
Hearthway Renovators Inc.
858-555-0174 Call/Text
BrightGableHomes.example
CSLB# 4087261
home owners
General Contractor

```html
<!DOCTYPE html>
<html lang="en">
<head>
<meta charset="utf-8">
<title>Hearthway Renovators – Door Hanger</title>
<link href="https://fonts.googleapis.com/css2?family=Cinzel:wght@500;600&family=Montserrat:wght@400;500;600&display=swap" rel="stylesheet">
<style>
  :root{
    --bg:#9a9a9a;
    --paper:#ffffff;
    --ink:#141414;
    --blue:#1a5ca8;
    --muted:#6a6a6a;
    --line:#e6e6e6;
    --serif:'Cinzel', serif;
    --sans:'Montserrat', sans-serif;
  }
  *{box-sizing:border-box;margin:0;padding:0}
  html,body{width:1138px;height:1200px;overflow:hidden;background:var(--bg)}
  .canvas{position:relative;width:1138px;height:1200px;background:var(--bg)}
  .panel{position:absolute;top:55px;width:489px;height:1090px;background:var(--paper);overflow:hidden}
  .panel--front{left:55px}
  .panel--back{left:594px}
  .photo{position:absolute}
  .photo--bath{left:44px;top:44px;width:400px;height:264px;background:linear-gradient(135deg,#f2f1ee 0%,#dcdad6 45%,#c9c6c1 70%,#eceae6 100%)}
  .photo--kitchen{left:43px;top:44px;width:400px;height:340px;background:linear-gradient(180deg,#d9d6d0 0%,#b9b3ab 45%,#ece9e4 62%,#7a6250 100%)}
  .brand{position:absolute;left:0;right:0;top:36px;text-align:center;font-family:var(--serif);font-size:8.5px;font-weight:600;color:#2b2b2b;letter-spacing:.4px}
  .heading{position:absolute;left:0;right:0;text-align:center;font-family:var(--serif);font-weight:600;font-size:20px;color:var(--ink);white-space:nowrap;line-height:28px}
  .heading em{font-style:normal;color:var(--blue)}
  .heading--left{text-align:left;left:49px}
  .address-box{position:absolute;left:49px;top:379px;width:390px;height:136px;background:#fff;border:1px solid #eee;box-shadow:0 0 6px rgba(0,0,0,.08)}
  .address-box__label{position:absolute;left:0;right:0;top:8px;text-align:center;font-family:var(--sans);font-size:11px;font-weight:500;color:var(--muted);letter-spacing:.3px}
  .feature{position:absolute;width:140px;margin-left:-70px;text-align:center;font-family:var(--sans);font-size:12.5px;color:var(--muted);line-height:19px}
  .feature .ring{display:block;width:50px;height:50px;margin:0 auto 12px;border:1.5px solid #333;border-radius:50%}
  .feature .ring svg{width:100%;height:100%}
  .divider{position:absolute;left:49px;top:720px;width:390px;height:1px;background:var(--line)}
  .subhead{position:absolute;left:50px;top:788px;font-family:var(--sans);font-weight:600;font-size:15.5px;color:var(--ink)}
  .services{position:absolute;left:50px;top:822px;list-style:none}
  .services li{display:flex;align-items:center;height:34.7px;font-family:var(--sans);font-size:16.5px;color:#333}
  .services svg{width:18px;height:18px;margin-right:15px;flex:none}
  .step-photo{position:absolute;top:468px;width:126px;height:96px}
  .step{position:absolute;top:572px;width:130px;margin-left:-65px;text-align:center}
  .step .label{font-family:var(--serif);font-weight:600;font-size:15px;color:var(--ink);line-height:24px}
  .step .label em{font-style:normal;color:var(--blue)}
  .step p{font-family:var(--sans);font-size:11.5px;color:var(--muted);line-height:19px;margin-top:-1px}
  .badge{position:absolute;top:675px;width:118px;height:51px;box-shadow:0 1px 5px rgba(0,0,0,.12)}
  .contact{position:absolute;top:978px;display:flex;align-items:center;font-family:var(--sans)}
  .contact .dot{width:38px;height:38px;border-radius:50%;background:var(--blue);border:3px solid #fff;box-shadow:0 0 0 2px #7aa7d8;display:flex;align-items:center;justify-content:center;margin-right:10px;flex:none}
  .contact .dot svg{width:18px;height:18px}
  .contact small{display:block;font-size:10px;color:var(--muted);line-height:14px}
  .contact strong{display:block;font-size:13px;font-weight:500;color:var(--ink);line-height:20px;white-space:nowrap}
  .contact-sep{position:absolute;left:213px;top:979px;width:1px;height:40px;background:var(--line)}
  .company-line{position:absolute;left:0;right:0;top:1040px;text-align:center;font-family:var(--sans);font-size:11px;font-weight:500;color:var(--muted);letter-spacing:.3px}
  .company-line strong{font-weight:600;color:var(--ink)}
</style>
</head>
<body>
<div class="canvas">

  <section class="panel panel--front">
    <div class="photo photo--bath" role="img" aria-label="Bright white remodelled bathroom with glass shower and gold fixtures, seen through a keyhole">
      <div class="brand">HEARTHWAY RENOVATORS</div>
    </div>

    <h2 class="heading" style="top:335px">YOUR <em>NEIGHBOR</em> JUST REMODELLED</h2>
    <div class="address-box"><div class="address-box__label">Come See Our Work at:</div></div>

    <h2 class="heading" style="top:547px;font-size:21px">LOVE YOUR <em>HOME</em> AGAIN!</h2>

    <div class="feature" style="left:106px;top:595px">
      <span class="ring"><svg viewBox="0 0 50 50" fill="none" stroke="#1a5ca8" stroke-width="1.6"><path d="M13 25 L25 14 L37 25 M16 23 V36 H34 V23"/><path d="M20 33 L30 22 M27 22 h4 v4"/></svg></span>
      We Make<br>Remodeling Easy
    </div>
    <div class="feature" style="left:246px;top:595px">
      <span class="ring"><svg viewBox="0 0 50 50" fill="none" stroke="#1a5ca8" stroke-width="1.6"><path d="M16 17 H34 M22 14 V20 M14 22 H36 V36 H14 Z"/><text x="25" y="33" font-family="Montserrat,sans-serif" font-size="10" font-weight="600" text-anchor="middle" fill="#1a5ca8" stroke="none">3D</text></svg></span>
      Free 3d<br>Design Services
    </div>
    <div class="feature" style="left:385px;top:595px">
      <span class="ring"><svg viewBox="0 0 50 50" fill="none" stroke="#1a5ca8" stroke-width="1.6"><rect x="15" y="13" width="14" height="22"/><rect x="25" y="19" width="12" height="16"/><path d="M18 18 h8 M18 22 h5 M18 26 h5 M28 23 h6 M28 27 h6 M28 31 h6"/></svg></span>
      Free Estimates
    </div>

    <div class="divider"></div>

    <h2 class="heading heading--left" style="top:749px">LICENSED <em>GENERAL</em> CONTRACTORS</h2>
    <div class="subhead">We Specialize in:</div>

    <ul class="services">
      <li><svg viewBox="0 0 18 18" fill="none" stroke="#1a5ca8" stroke-width="1.1"><rect x="2" y="3" width="14" height="5"/><rect x="2" y="10" width="14" height="6"/><path d="M9 10 v6"/></svg>-Kitchen Remodel</li>
      <li><svg viewBox="0 0 18 18" fill="none" stroke="#1a5ca8" stroke-width="1.1"><rect x="2" y="8" width="14" height="8"/><path d="M5 8 V3 h4 M9 12 h7 M9 8 v8"/></svg>-Bathroom Remodel</li>
      <li><svg viewBox="0 0 18 18" fill="none" stroke="#1a5ca8" stroke-width="1.1"><rect x="3" y="2" width="11" height="4"/><path d="M14 4 h2 v4 H9 v2 M8 10 h2 v6 H8 Z"/></svg>-Interior/Exterior Painting</li>
      <li><svg viewBox="0 0 18 18" fill="none" stroke="#1a5ca8" stroke-width="1.1"><rect x="2" y="4" width="12" height="12"/><path d="M5 2 H16 V13 M2 12 L10 4 M6 16 L14 8"/></svg>-Flooring: Carpet, Vinyl, Wood &amp; Tile</li>
      <li><svg viewBox="0 0 18 18" fill="none" stroke="#1a5ca8" stroke-width="1.1"><circle cx="9" cy="9" r="6"/><path d="M9 1 v2 M9 15 v2 M1 9 h2 M15 9 h2 M10 5 L7 9.5 h3 L8 13"/></svg>-Energy Efficient Upgrades</li>
      <li><svg viewBox="0 0 18 18" fill="none" stroke="#1a5ca8" stroke-width="1.1"><rect x="2" y="2" width="14" height="14"/><rect x="4" y="4" width="4" height="12"/><rect x="10" y="4" width="4" height="12"/></svg>-Window/Door Replacement</li>
      <li><svg viewBox="0 0 18 18" fill="none" stroke="#1a5ca8" stroke-width="1.1"><path d="M9 2 C6 7 4 9 4 12 a5 5 0 0 0 10 0 C14 9 12 7 9 2 Z"/></svg>-Water &amp; Mold Damage</li>
    </ul>
  </section>

  <section class="panel panel--back">
    <div class="photo photo--kitchen" role="img" aria-label="Grey shaker kitchen with white island, pendant lights and wood floor">
      <div class="brand">HEARTHWAY RENOVATORS</div>
    </div>

    <h2 class="heading" style="top:419px;font-size:21px"><em>GET STARTED</em> IN 3 SIMPLE STEPS:</h2>

    <div class="step-photo" style="left:50px;background:linear-gradient(180deg,#cfd3cf 0%,#b8a48a 55%,#d99a2b 100%)" role="img" aria-label="Sold sign in front of a house"></div>
    <div class="step-photo" style="left:182px;background:linear-gradient(180deg,#dfe3e6 0%,#9fae8f 55%,#7fa2c4 100%)" role="img" aria-label="Estimator with clipboard outside a home"></div>
    <div class="step-photo" style="left:313px;background:linear-gradient(135deg,#d9c8a8 0%,#c9b48e 45%,#eeeeee 55%,#f8f8f8 100%)" role="img" aria-label="Kitchen photo blending into a design sketch"></div>

    <div class="step" style="left:113px"><div class="label">STEP: <em>01</em></div><p>Order Free Estimate<br>and Design</p></div>
    <div class="step" style="left:245px"><div class="label">STEP: <em>02</em></div><p>Approve Estimate<br>and Design</p></div>
    <div class="step" style="left:376px;width:140px;margin-left:-70px"><div class="label">STEP: <em>03</em></div><p>Hearthway Renovators<br>Builds Your Dream</p></div>

    <div class="badge" style="left:49px;background:#0d0d0d"></div>
    <div class="badge" style="left:184px;background:#f4f4f4"></div>
    <div class="badge" style="left:319px;background:#fafafa"></div>

    <h2 class="heading" style="top:772px;font-size:21px">THINKING <em>ABOUT</em> SELLING?</h2>

    <div class="feature" style="left:105px;top:820px">
      <span class="ring"><svg viewBox="0 0 50 50" fill="none" stroke="#1a5ca8" stroke-width="1.6"><path d="M22 20 L29 14 L36 20 M24 19 V26 H34 V19"/><path d="M12 30 h7 l6 3 h7 a2 2 0 0 1 0 4 H22 M12 36 l8 2 h10 l8-6"/></svg></span>
      We Buy Homes
    </div>
    <div class="feature" style="left:239px;top:820px">
      <span class="ring"><svg viewBox="0 0 50 50" fill="none" stroke="#1a5ca8" stroke-width="1.6"><circle cx="26" cy="19" r="6"/><path d="M26 15 v8 M24 17 h3.5 M24 21 h3.5"/><path d="M12 30 h7 l6 3 h7 a2 2 0 0 1 0 4 H22 M12 36 l8 2 h10 l8-6"/></svg></span>
      Get Cash Offer
    </div>
    <div class="feature" style="left:381px;top:820px">
      <span class="ring"><svg viewBox="0 0 50 50" fill="none" stroke="#1a5ca8" stroke-width="1.6"><path d="M19 19 L25 14 L31 19 M21 18 V24 H29 V18"/><path d="M12 28 l6-2 l7 5 l7-5 l6 2 M18 30 l6 5 h4 l5-5"/></svg></span>
      Selling Made Easy
    </div>

    <h2 class="heading" style="top:929px;font-size:21px"><em>CALL</em> NOW!!</h2>

    <div class="contact" style="left:49px">
      <span class="dot"><svg viewBox="0 0 18 18" fill="#fff"><path d="M4 2 l3 0 l1 4 l-2 1.5 a9 9 0 0 0 4.5 4.5 L12 10 l4 1 v3 a2 2 0 0 1-2 2 A12 12 0 0 1 2 4 a2 2 0 0 1 2-2 Z"/></svg></span>
      <div><small>Call or Text</small><strong>858-555-0174</strong></div>
    </div>
    <div class="contact-sep"></div>
    <div class="contact" style="left:236px">
      <span class="dot"><svg viewBox="0 0 18 18" fill="none" stroke="#fff" stroke-width="1.3"><circle cx="9" cy="9" r="7"/><path d="M2 9 h14 M9 2 c-3 4-3 10 0 14 M9 2 c3 4 3 10 0 14"/></svg></span>
      <div><small>Website</small><strong>BrightGableHomes.example</strong></div>
    </div>

    <div class="company-line"><strong>Hearthway Renovators Inc.</strong> &nbsp;|&nbsp; CSLB# 4087261</div>
  </section>

</div>
</body>
</html>
```